Austrian finance und insurance broker needs business card design

We Need a serious looking Design for Business Card. we consult private and corporates customers in finance and insurance questions. the final design should express security and experience. We consult customers in questions of loans, Investments and insurance and have a wide range of Banks to offer. We compare several offers and select the best for our customers.

Target Market(s)

private and coporate customers with efforts in Money and insurance

Industry/Entity Type

Insurance Broker

Contact Information for Business Card

Bernhard Aigner
Geschäftsführer
staatl. geprüfter Vermögensberater und Versicherungsmakler
Tel: 0664 521 8409
office@der-brandl.at
www.der-brandl.at
Leopold Hainz Gasse 14
2183 Melkstetten
GISA Nr. 48270315 u. 51736048 (backside)

Font styles to use
Serif
Sans Serif

Requirements
Must have
• logo (designcrowd zip) and all Details
Nice to have
• makler logo design, maybe a 2 coloured Version is possible

```html
<!DOCTYPE html>
<html lang="de">
<head>
<meta charset="utf-8">
<title>Visitenkarte – Aigner Vermögensberatung GmbH</title>
<link rel="stylesheet" href="https://fonts.googleapis.com/css2?family=Lato:wght@400;700&family=Nunito:wght@600;700;800&display=swap">
<style>
  :root {
    --backdrop: #e9e4dc;
    --card-light: #d2ab7d;
    --card-mid: #c29667;
    --card-dark: #b08055;
    --ink: #141210;
    --band: #0b0a09;
    --band-text: #ffffff;
    --seal: #b3243a;
    --seal-dark: #7e1526;
  }
  * { margin: 0; padding: 0; box-sizing: border-box; }
  html, body {
    width: 1200px; height: 900px; overflow: hidden;
    background: var(--backdrop);
  }
  .canvas { position: relative; width: 1200px; height: 900px; }

  .card {
    position: absolute;
    background: linear-gradient(160deg, var(--card-light) 0%, var(--card-mid) 55%, var(--card-dark) 100%);
    color: var(--ink);
    font-family: "Lato", Arial, sans-serif;
    overflow: visible;
  }
  .card--front { left: 330px; top: 90px; width: 555px; height: 343px; text-align: center; }
  .card--back  { left: 330px; top: 469px; width: 559px; height: 343px; }

  .front__line { position: absolute; left: 0; width: 100%; line-height: 1; }
  .holder-name { top: 44px; font-family: "Nunito", Arial, sans-serif; font-weight: 700; font-size: 21px; }
  .holder-role { font-size: 16px; }
  .holder-role--1 { top: 70px; }
  .holder-role--2 { top: 92px; }
  .holder-role--3 { top: 113px; }

  .divider { position: absolute; height: 1px; background: var(--ink); }
  .divider--left  { left: 189px; top: 155px; width: 53px; }
  .divider--right { left: 312px; top: 155px; width: 55px; }
  .divider--full  { left: 189px; top: 248px; width: 178px; }

  .contact-icons { position: absolute; left: 244px; top: 147px; display: flex; gap: 6px; }
  .contact-icons svg { display: block; }

  .contact { font-size: 16px; }
  .contact--phone { top: 176px; }
  .contact--mail  { top: 197px; }
  .contact--web   { top: 218px; }
  .address { font-size: 16px; }
  .address--street { top: 263px; }
  .address--city   { top: 284px; }

  .brand { position: absolute; left: 110px; top: 124px; display: flex; align-items: center; gap: 16px; }
  .brand__dot { width: 20px; height: 20px; border-radius: 50%; background: var(--ink); }
  .brand__text { display: flex; flex-direction: column; gap: 6px; }
  .brand__name { font-family: "Nunito", Arial, sans-serif; font-weight: 700; font-size: 19px; line-height: 1; }
  .brand__tagline { font-family: "Nunito", Arial, sans-serif; font-weight: 700; font-size: 13.5px; line-height: 1; }

  .legal-band {
    position: absolute; left: 0; top: 262px; width: 100%; height: 56px;
    background: var(--band);
  }
  .legal-band__text {
    position: absolute; left: 53px; top: 19px;
    color: var(--band-text); font-size: 16px; line-height: 1;
  }
  .partner-seal {
    position: absolute; left: 433px; top: 226px; width: 64px; height: 64px;
    border-radius: 50%;
    background: radial-gradient(circle at 40% 35%, var(--seal) 0%, var(--seal) 55%, var(--seal-dark) 100%);
  }
</style>
</head>
<body>
<main class="canvas">
  <section class="card card--front" aria-label="Visitenkarte Vorderseite">
    <p class="front__line holder-name">Bernhard Aigner</p>
    <p class="front__line holder-role holder-role--1">Geschäftsführer</p>
    <p class="front__line holder-role holder-role--2">staatl. geprüfter Vermögensberater</p>
    <p class="front__line holder-role holder-role--3">und Versicherungsmakler</p>

    <span class="divider divider--left"></span>
    <div class="contact-icons" aria-hidden="true">
      <svg width="18" height="16" viewBox="0 0 18 16"><rect width="18" height="16" fill="#141210"/><path d="M4 6 Q9 2 14 6 L12 7 L11 5.5 L7 5.5 L6 7 Z M5 8 H13 V12 H5 Z" fill="#d2ab7d"/></svg>
      <svg width="18" height="16" viewBox="0 0 18 16"><rect width="18" height="16" fill="#141210"/><rect x="4" y="4.5" width="10" height="7" fill="none" stroke="#d2ab7d" stroke-width="1.2"/><path d="M4 4.5 L9 8.5 L14 4.5" fill="none" stroke="#d2ab7d" stroke-width="1.2"/></svg>
      <svg width="18" height="16" viewBox="0 0 18 16"><rect width="18" height="16" fill="#141210"/><circle cx="9" cy="8" r="4.5" fill="none" stroke="#d2ab7d" stroke-width="1.2"/><path d="M4.5 8 H13.5 M9 3.5 Q6.5 8 9 12.5 Q11.5 8 9 3.5" fill="none" stroke="#d2ab7d" stroke-width="1"/></svg>
    </div>
    <span class="divider divider--right"></span>

    <p class="front__line contact contact--phone">0664 521 8409</p>
    <p class="front__line contact contact--mail">office@der-brandl.at</p>
    <p class="front__line contact contact--web">www.der-brandl.at</p>

    <span class="divider divider--full"></span>

    <p class="front__line address address--street">Leopold Hainz Gasse 14</p>
    <p class="front__line address address--city">2183 Melkstetten</p>
  </section>

  <section class="card card--back" aria-label="Visitenkarte Rückseite">
    <div class="brand">
      <span class="brand__dot" aria-hidden="true"></span>
      <div class="brand__text">
        <p class="brand__name">Aigner Vermögensberatung GmbH</p>
        <p class="brand__tagline">Finanzieren, Versichern, Vorsorgen</p>
      </div>
    </div>
    <div class="legal-band">
      <p class="legal-band__text">GISA Nr. 48270315 u. 51736048</p>
    </div>
    <div class="partner-seal" role="img" aria-label="Abzeichen des Maklerverbands"></div>
  </section>
</main>
</body>
</html>
```